BrambleWorks business card

Looking for business card design that supports our company/software values. We have 2 logo designs at the moment but open to change if you think you can enhance the brand. Check out website www.brambleworks.com.au.

Target Market(s)

Education

Contact Information for Business Card

Name, title, mobile, email and website

Font styles to use
Sans Serif

Colors

Designer to choose colors to be used in the design.

Requirements
Must have
• BrambleWorks logo with tree and tagline on rear side with dark grey background colour

```html
<!DOCTYPE html>
<html lang="en">
<head>
<meta charset="utf-8">
<title>BrambleWorks Business Card</title>
<link rel="stylesheet" href="https://fonts.googleapis.com/css2?family=Montserrat:wght@400;500;600;800&display=swap">
<style>
  :root {
    --page-bg: #e9eaec;
    --brand-blue: #1866a0;
    --brand-yellow: #fbb634;
    --brand-grey: #515350;
    --card-white: #ffffff;
    --text-light: #ffffff;
  }
  * { box-sizing: border-box; margin: 0; padding: 0; }
  html, body {
    width: 1200px; height: 900px; overflow: hidden;
    background: var(--page-bg);
    font-family: "Montserrat", sans-serif;
  }
  .canvas {
    width: 1200px; height: 900px;
    display: flex; flex-direction: column; align-items: center; justify-content: center;
    gap: 40px;
  }
  .card {
    position: relative;
    width: 700px; height: 400px;
    overflow: hidden;
    box-shadow: 0 6px 18px rgba(0,0,0,0.12);
  }
  /* Front */
  .card-front {
    background: var(--brand-blue);
    display: flex; align-items: center; justify-content: center;
  }
  .front-brand {
    display: flex; align-items: center; gap: 18px;
    color: var(--brand-yellow);
    font-weight: 800; font-size: 50px; letter-spacing: -0.5px;
  }
  .front-brand .brand-dot {
    width: 46px; height: 46px; border-radius: 50%;
    background: var(--brand-yellow);
  }
  /* Back */
  .card-back { background: var(--card-white); }
  .card-back .wave { position: absolute; inset: 0; width: 100%; height: 100%; }
  .back-brand {
    position: absolute; left: 50px; top: 110px;
    display: flex; align-items: center; gap: 10px;
    color: var(--brand-grey);
    font-weight: 600; font-size: 26px;
  }
  .back-brand .brand-dot {
    width: 22px; height: 22px; border-radius: 50%;
    background: var(--brand-grey);
  }
  .person {
    position: absolute; right: 60px; top: 56px;
    text-align: right;
  }
  .person-name {
    color: var(--brand-grey);
    font-weight: 800; font-size: 28px; line-height: 1.1;
    white-space: nowrap;
  }
  .person-title {
    color: var(--text-light);
    font-weight: 400; font-size: 15px; letter-spacing: 0.5px;
    margin-top: 2px;
  }
  .title-rule {
    display: block; width: 30px; height: 3px;
    background: var(--brand-grey);
    margin: 8px 0 0 auto;
  }
  .contact-list {
    position: absolute; right: 34px; top: 165px;
    list-style: none;
    color: var(--text-light);
    font-size: 15px; line-height: 1;
  }
  .contact-list li {
    display: flex; align-items: center; justify-content: flex-end; gap: 14px;
    margin-bottom: 12px;
  }
  .contact-list svg { width: 18px; height: 18px; flex: none; }
  .address {
    position: absolute; left: 230px; bottom: 30px;
    color: var(--text-light);
    font-size: 14px; line-height: 1.5;
    font-style: normal;
  }
</style>
</head>
<body>
<main class="canvas">
  <section class="card card-front" aria-label="Card front">
    <div class="front-brand"><span class="brand-dot"></span>BrambleWorks</div>
  </section>

  <section class="card card-back" aria-label="Card back">
    <svg class="wave" viewBox="0 0 700 400" preserveAspectRatio="none" aria-hidden="true">
      <path d="M0 340 C 170 330, 260 250, 320 160 C 380 60, 460 10, 560 0 L700 0 L700 400 L0 400 Z" fill="var(--brand-blue)"/>
      <path d="M0 340 C 170 330, 260 250, 320 160 C 380 60, 460 10, 560 0" fill="none" stroke="var(--brand-grey)" stroke-width="6"/>
    </svg>

    <div class="back-brand"><span class="brand-dot"></span>BrambleWorks</div>

    <div class="person">
      <div class="person-name">Daniel Corwin</div>
      <div class="person-title">FOUNDER</div>
      <span class="title-rule"></span>
    </div>

    <ul class="contact-list">
      <li>000 000 0000
        <svg viewBox="0 0 24 24" aria-hidden="true"><path d="M6.6 10.8a15 15 0 0 0 6.6 6.6l2.2-2.2a1 1 0 0 1 1-.25 11.4 11.4 0 0 0 3.6.57 1 1 0 0 1 1 1V20a1 1 0 0 1-1 1A17 17 0 0 1 3 4a1 1 0 0 1 1-1h3.5a1 1 0 0 1 1 1c0 1.25.2 2.45.57 3.57a1 1 0 0 1-.25 1z" fill="var(--brand-grey)"/></svg>
      </li>
      <li>info@yourmailwebsite.com
        <svg viewBox="0 0 24 24" aria-hidden="true"><rect x="2" y="5" width="20" height="14" fill="var(--brand-grey)"/><path d="M2 5l10 8 10-8" fill="none" stroke="#ffffff" stroke-width="1.5"/></svg>
      </li>
      <li>www.brambleworks.com.au
        <svg viewBox="0 0 24 24" aria-hidden="true"><circle cx="12" cy="12" r="10" fill="var(--brand-grey)"/><path d="M2 12h20M12 2c3 3 3 17 0 20M12 2c-3 3-3 17 0 20" fill="none" stroke="#ffffff" stroke-width="1.2"/></svg>
      </li>
    </ul>

    <address class="address">
      PO Box 218 Ashvale, 4810<br>
      14-18 Kestrel Road, Ashvale, 4815
    </address>
  </section>
</main>
</body>
</html>
```